Business Card for Pottery and Jewellery Designer

A new business card design is needed to accompany a newly launching pottery and jewellery website. The company logo has been attached for use. The company is called Glazewick Studio. For a sense of the vibe please see the website (it is currently under construction but this way you'll get a feel for the style) www.GlazewickStudio.com

The website font is Pontano Sans for the body of the text with Overlock for headers.

The overall look should be clean and elegant. The back side can have just the logo. The front side should have a smaller logo and the following details displayed:

Glazewick Studio
Designer: Hollis Marrow
Phone: xxx.xxx.xxxx
Email: Designer@GlazewickStudio.com

The structure of displaying this is completely up to you. Different layouts and creative methods of displaying contact info are welcome as long as it stays clean/uncluttered.

No product photographs are to be included in the design as the catalogue changes quickly.

Colour preferences lean towards elegant and understated (charcoal grey, dark navy blue etc.)

Please let me know if you have any further questions or further details required.

Target Market(s)

Target market is 30+ year old women

Industry/Entity Type

Construction

Colors
ffffff
1b1b1b
474747
d9d9d9
fafafa
0355a3

Requirements
Must have
• The submissions so far have looked very typical and don't stand out right now. They're also all in navy with very little variation. I'm looking for something that stands out a it more while still being clean-looking.
Nice to have
• I've attached a few design samples and an idea for a backdrop. It would be great to see some designs in black, white, and grey with only a hint of color.
Should not have
• Product Images

```html
<!DOCTYPE html>
<html lang="en">
<head>
<meta charset="utf-8">
<title>Glazewick Studio – Business Card</title>
<link rel="stylesheet" href="https://fonts.googleapis.com/css2?family=Exo+2:wght@400;500&display=swap">
<style>
  :root {
    --backdrop: #e9e8e6;
    --card: #ffffff;
    --charcoal: #1b1b1b;
    --graphite: #474747;
    --accent-blue: #0355a3;
    --text-light: #fafafa;
    --shadow: rgba(0, 0, 0, 0.18);
  }
  * { margin: 0; padding: 0; box-sizing: border-box; }
  html, body {
    width: 1200px;
    height: 900px;
    overflow: hidden;
    background: var(--backdrop);
    font-family: "Exo 2", sans-serif;
  }
  .card {
    position: absolute;
    left: 100px;
    top: 165px;
    width: 1000px;
    height: 571px;
    background: var(--card);
    box-shadow: 0 10px 30px var(--shadow);
    overflow: hidden;
  }
  .card-swoosh {
    position: absolute;
    inset: 0;
    width: 100%;
    height: 100%;
  }
  .brand {
    position: absolute;
    left: 70px;
    top: 70px;
    display: flex;
    align-items: center;
    gap: 22px;
  }
  .brand-dot {
    width: 64px;
    height: 64px;
    border-radius: 50%;
    background: var(--charcoal);
  }
  .brand-name {
    font-family: "Exo 2", sans-serif;
    font-weight: 400;
    font-size: 44px;
    letter-spacing: 3px;
    color: var(--charcoal);
    text-transform: uppercase;
  }
  .contact-list {
    position: absolute;
    right: 40px;
    top: 200px;
    list-style: none;
    text-align: right;
    color: var(--text-light);
    font-size: 17px;
    line-height: 1.35;
  }
  .contact-item {
    display: flex;
    justify-content: flex-end;
    align-items: center;
    gap: 10px;
    margin-bottom: 11px;
  }
  .contact-icon {
    width: 18px;
    height: 18px;
    flex: none;
  }
  .holder {
    position: absolute;
    left: 270px;
    top: 462px;
    color: var(--text-light);
  }
  .holder-name {
    font-size: 27px;
    font-weight: 500;
    letter-spacing: 2px;
    text-transform: uppercase;
  }
  .holder-role {
    font-size: 18px;
    margin-top: 2px;
  }
</style>
</head>
<body>
  <main class="card">
    <svg class="card-swoosh" viewBox="0 0 1000 571" aria-hidden="true">
      <path d="M175 571 C340 360 590 215 1000 175 L1000 571 Z" fill="var(--charcoal)"/>
      <path d="M142 571 C310 345 570 195 1000 150" fill="none" stroke="var(--accent-blue)" stroke-width="8"/>
      <path d="M116 571 C285 332 550 178 1000 130" fill="none" stroke="var(--graphite)" stroke-width="3"/>
    </svg>

    <div class="brand">
      <span class="brand-dot"></span>
      <span class="brand-name">Glazewick Studio</span>
    </div>

    <ul class="contact-list">
      <li class="contact-item">
        <span>41 Kiln Row, Suite 2<br>Eastmarsh Lane</span>
        <svg class="contact-icon" viewBox="0 0 24 24" fill="#fafafa"><path d="M6.6 10.8a15 15 0 0 0 6.6 6.6l2.2-2.2a1 1 0 0 1 1-.25 11.4 11.4 0 0 0 3.6.6 1 1 0 0 1 1 1V20a1 1 0 0 1-1 1A17 17 0 0 1 3 4a1 1 0 0 1 1-1h3.5a1 1 0 0 1 1 1 11.4 11.4 0 0 0 .6 3.6 1 1 0 0 1-.25 1z"/></svg>
      </li>
      <li class="contact-item">
        <span>555 014 2290</span>
        <svg class="contact-icon" viewBox="0 0 24 24" fill="none" stroke="#fafafa" stroke-width="2"><rect x="7" y="2" width="10" height="20" rx="2"/><line x1="11" y1="18" x2="13" y2="18"/></svg>
      </li>
      <li class="contact-item">
        <span>555 014 2291</span>
        <svg class="contact-icon" viewBox="0 0 24 24" fill="#fafafa"><rect x="4" y="9" width="16" height="11" rx="1"/><rect x="7" y="3" width="10" height="6"/></svg>
      </li>
      <li class="contact-item">
        <span>555 014 2292</span>
        <svg class="contact-icon" viewBox="0 0 24 24" fill="none" stroke="#fafafa" stroke-width="2"><rect x="3" y="5" width="18" height="14"/><path d="M3 5l9 8 9-8"/></svg>
      </li>
      <li class="contact-item">
        <span>Designer@GlazewickStudio.com</span>
        <svg class="contact-icon" viewBox="0 0 24 24" fill="none" stroke="#fafafa" stroke-width="2"><circle cx="12" cy="12" r="9"/><path d="M3 12h18M12 3c3 3 3 15 0 18M12 3c-3 3-3 15 0 18"/></svg>
      </li>
      <li class="contact-item">
        <span>www.GlazewickStudio.com</span>
      </li>
    </ul>

    <div class="holder">
      <p class="holder-name">Hollis Marrow</p>
      <p class="holder-role">Managing Director</p>
    </div>
  </main>
</body>
</html>
```